The dental corner of brindlewood web page

website for dental office
Already have domain, mostly information only with address, telephone and google map and hours of operation on top. mobile friendly. SEO a most.

Target Market(s)

Local families

Industry/Entity Type

Dental Clinic

Number of Pages Required

1 page

Font styles to use
Serif

Colors

Designer to choose colors to be used in the design.

Requirements
Must have
• SEO
• Information to find the location
• mobile friendly
• dr's. biography
• services offered
• contect to social media (google, facebook, and instagram)
• Se habla espaƱol
• All insurance accepted
• request an appointment form to notify us

```html
<!DOCTYPE html>
<html lang="en">
<head>
<meta charset="utf-8">
<meta name="viewport" content="width=1200">
<title>The Dental Corner of Brindlewood</title>
<link rel="stylesheet" href="https://fonts.googleapis.com/css2?family=Raleway:ital,wght@0,400;0,500;0,600;0,700;1,400;1,500;1,600&family=Roboto:wght@400;500;700&display=swap">
<style>
:root{
  --blue:#1b5fb0;
  --navy:#0f4a93;
  --green:#8cc63f;
  --green-dark:#74ad2c;
  --text:#555b63;
  --light:#f2f5f9;
  --dark:#262829;
  --bar:#4f5153;
  --white:#ffffff;
}
*{margin:0;padding:0;box-sizing:border-box}
html,body{width:1200px;height:4010px;overflow:hidden}
body{position:relative;font-family:'Roboto',sans-serif;color:var(--text);background:var(--white)}
.abs{position:absolute}
.brand{font-family:'Raleway',sans-serif;font-weight:700;color:var(--navy);letter-spacing:.5px}

/* header */
.site-header{position:absolute;left:0;top:0;width:1200px;height:157px;background:var(--white)}
.site-header .brand{left:130px;top:52px;font-size:22px;line-height:26px;width:230px}
.main-nav{position:absolute;top:70px;left:490px;display:flex;gap:44px;font-family:'Raleway',sans-serif;font-weight:700;font-size:16px;color:var(--navy)}
.main-nav .active{color:var(--green)}

/* hero */
.hero{position:absolute;left:0;top:157px;width:1200px;height:680px;background:linear-gradient(100deg,#6f93c4 0%,#8fb0d8 40%,#6d95c9 70%,#4f7db8 100%)}
.info-bar{position:absolute;top:36px;left:0;width:1200px;height:50px}
.info-item{position:absolute;display:flex;align-items:center;gap:14px;color:var(--white);font-size:14px;line-height:18px}
.info-item b{font-weight:700}
.info-icon{width:36px;height:36px;border-radius:50%;background:var(--navy);display:flex;align-items:center;justify-content:center}
.hero-title{position:absolute;left:130px;top:178px;width:470px;text-align:center;color:var(--white)}
.hero-title .welcome{font-family:'Raleway',sans-serif;font-style:italic;font-size:40px}
.hero-title .brand{color:var(--white);font-size:40px;line-height:48px;margin-top:10px}
.hero-title .brand small{display:block;font-size:24px;line-height:30px}
.hero-title .tagline{font-family:'Raleway',sans-serif;font-size:34px;line-height:42px;margin-top:22px}
.btn{display:inline-block;background:var(--green);color:var(--white);font-family:'Raleway',sans-serif;text-align:center;border-radius:6px}
.hero .btn{position:absolute;left:237px;top:449px;width:243px;height:51px;line-height:51px;font-size:24px;font-weight:600}
.consult{position:absolute;left:780px;top:192px;width:250px;height:314px;background:rgba(40,44,50,.82);border-radius:10px;padding:22px 20px;color:var(--white)}
.consult h3{font-family:'Raleway',sans-serif;font-size:22px;font-weight:700;margin-bottom:18px}
.consult label{display:block;font-size:13px;margin-bottom:4px}
.consult .field{height:32px;background:var(--white);border-radius:3px;margin-bottom:14px;font-size:13px;color:#666;line-height:32px;padding-left:8px}
.consult .btn{width:140px;height:28px;line-height:28px;font-size:13px;font-weight:600;border-radius:4px}

/* about */
.about{position:absolute;left:0;top:837px;width:1200px;height:529px;background:var(--white)}
.about .welcome-to{position:absolute;left:180px;top:118px;font-family:'Raleway',sans-serif;font-style:italic;font-size:22px;color:var(--navy)}
.about .brand{position:absolute;left:180px;top:146px;font-size:24px;line-height:28px}
.about .mark{position:absolute;left:110px;top:120px;width:60px;height:60px;border-radius:50%;background:var(--blue)}
.about p{position:absolute;left:114px;width:460px;font-size:14px;line-height:21px}
.about .btn{position:absolute;left:114px;top:392px;width:120px;height:30px;line-height:30px;font-size:14px;font-weight:600;border-radius:4px}
.video{position:absolute;left:634px;top:92px;width:486px;height:337px;background:#000}
.video-still{position:absolute;left:0;top:24px;width:486px;height:280px;background:linear-gradient(110deg,#d9dfe6,#b9c6d3 50%,#e6e9ec)}
.play{position:absolute;left:213px;top:140px;width:60px;height:42px;background:rgba(20,20,20,.85);border-radius:10px}

/* call to action */
.smile{position:absolute;left:0;top:1366px;width:1200px;height:506px;background:linear-gradient(90deg,#e9edf2,#dfe6ee)}
.smile-photo{position:absolute;left:0;top:0;width:600px;height:506px;background:linear-gradient(120deg,#c9d4de,#eef0f2 50%,#d2d9e1)}
.smile h2{position:absolute;left:600px;width:600px;text-align:center;font-family:'Raleway',sans-serif;font-style:italic;color:var(--navy)}
.smile .h-light{top:80px;font-size:56px;font-weight:400}
.smile .h-bold{top:142px;font-size:64px;font-weight:700}
.call-box{position:absolute;left:609px;top:228px;width:491px;height:126px;background:var(--green);border-radius:6px;text-align:center;color:var(--navy)}
.call-box .label{font-family:'Roboto',sans-serif;font-weight:700;font-size:27px;margin-top:14px;letter-spacing:.5px}
.call-box .phone{font-family:'Roboto',sans-serif;font-weight:700;font-size:52px;line-height:60px}
.keep{position:absolute;font-family:'Raleway',sans-serif;color:var(--navy)}
.smile .keep{left:600px;width:600px;top:382px;text-align:center;font-size:28px;font-weight:500}
.socials{position:absolute;display:flex;gap:8px}
.socials span{display:block;border-radius:50%;border:2px solid currentColor}
.smile .socials{left:800px;top:430px;color:var(--navy)}
.smile .socials span{width:30px;height:30px}

/* services */
.services{position:absolute;left:0;top:1872px;width:1200px;height:800px;background:linear-gradient(110deg,#8cc63f 0%,#9fd05a 45%,#7fbd38 100%)}
.services h2{position:absolute;left:0;width:1200px;top:66px;text-align:center;font-family:'Raleway',sans-serif;font-style:italic;font-weight:500;font-size:46px;color:var(--navy)}
.services h3{position:absolute;left:66px;top:180px;font-family:'Roboto',sans-serif;font-weight:700;font-size:20px;color:var(--navy)}
.services .intro{position:absolute;left:66px;top:222px;width:1065px;font-size:14px;line-height:20px;color:#33402a}
.card{position:absolute;top:334px;width:343px;height:388px;background:var(--white)}
.card .icon{position:absolute;left:34px;top:40px}
.card h4{position:absolute;left:110px;top:38px;width:210px;text-align:center;font-family:'Raleway',sans-serif;font-weight:500;font-size:26px;line-height:30px;color:var(--navy)}
.card ul{position:absolute;left:42px;top:144px;list-style:none;font-size:17px;line-height:30px;color:#555}
.card li{display:flex;align-items:center;gap:16px}
.card .plus{position:absolute;left:147px;top:366px;width:48px;height:48px;border-radius:50%;background:var(--navy)}

/* testimonials */
.testimonials{position:absolute;left:0;top:2672px;width:1200px;height:485px;background:linear-gradient(110deg,#2f6fc2,#2661ad 50%,#2d6ab8)}
.testimonials h2{position:absolute;left:0;width:1200px;top:66px;text-align:center;font-family:'Raleway',sans-serif;font-weight:500;font-size:46px;color:var(--white)}
.avatar{position:absolute;width:90px;height:90px;border-radius:50%;background:#c9d3de;border:4px solid var(--white)}
.quote{position:absolute;top:199px;width:343px;height:129px;border:2px solid rgba(255,255,255,.7);padding:16px 18px;color:var(--white);font-size:13px;line-height:19px}
.quote .name{margin-top:10px}

/* map */
.map{position:absolute;left:0;top:3157px;width:1200px;height:352px;background:linear-gradient(120deg,#e8ece4,#f1f1ec 40%,#e4e8ee 80%,#dfe6dc)}
.map-label{position:absolute;left:100px;top:150px;display:flex;align-items:center;gap:8px;font-family:'Raleway',sans-serif;font-weight:700;font-size:15px;color:var(--navy)}

/* footer */
.site-footer{position:absolute;left:0;top:3509px;width:1200px;height:405px;background:var(--dark);color:#d6d6d6}
.site-footer .brand{position:absolute;left:100px;top:130px;width:230px;text-align:center;color:var(--white);font-size:22px;line-height:26px}
.spanish{position:absolute;left:151px;top:340px;width:112px;height:54px;border:2px solid var(--white);color:var(--white);text-align:center;font-family:'Roboto',sans-serif;font-weight:700;font-size:16px;line-height:22px;padding-top:4px}
.foot-col{position:absolute;top:100px}
.foot-col h4{font-family:'Raleway',sans-serif;font-weight:700;font-size:18px;color:var(--green);margin-bottom:20px}
.foot-col p{font-size:14px;line-height:20px}
.foot-col .addr-title{color:var(--green);font-weight:700;font-size:15px}
.foot-col .call-label{margin-top:34px;color:var(--green);font-size:17px}
.foot-col .call-phone{font-size:30px;font-weight:700;color:var(--white);margin-top:4px}
.site-footer .btn{width:170px;height:28px;line-height:28px;font-size:13px;font-weight:600;border-radius:3px;margin-top:14px}
.site-footer .keep{position:static;color:var(--green);font-size:17px;margin-top:34px}
.site-footer .socials{position:static;margin-top:6px;color:var(--white)}
.site-footer .socials span{width:22px;height:22px}
.insurance{margin-top:22px;display:flex;align-items:center;gap:8px;color:var(--green);font-weight:700;font-size:22px}
.copyright{position:absolute;left:0;top:3914px;width:1200px;height:96px;background:var(--bar);color:#d9d9d9;font-size:14px;text-align:center;line-height:96px}
</style>
</head>
<body>

<header class="site-header">
  <div class="abs brand">THE DENTAL CORNER<br>OF BRINDLEWOOD</div>
  <nav class="main-nav">
    <span class="active">HOME</span>
    <span>ABOUT US ▾</span>
    <span>SERVICES ▾</span>
    <span>TESTIMONIALS ▾</span>
    <span>CONTACT US ▾</span>
  </nav>
</header>

<section class="hero" role="img" aria-label="Dentist showing an x-ray to a young patient in a bright clinic">
  <div class="info-bar">
    <div class="info-item" style="left:145px">
      <span class="info-icon"><svg width="18" height="18" viewBox="0 0 24 24"><path fill="#fff" d="M6.6 10.8a15 15 0 0 0 6.6 6.6l2.2-2.2c.3-.3.7-.4 1-.2 1.1.4 2.3.6 3.6.6.6 0 1 .4 1 1V20c0 .6-.4 1-1 1A17 17 0 0 1 3 4c0-.6.4-1 1-1h3.5c.6 0 1 .4 1 1 0 1.3.2 2.5.6 3.6.1.3 0 .7-.2 1z"/></svg></span>
      <div>For appointment call<br><b>213-555-0190</b></div>
    </div>
    <div class="info-item" style="left:530px">
      <span class="info-icon"><svg width="18" height="18" viewBox="0 0 24 24"><circle cx="12" cy="12" r="9" fill="none" stroke="#fff" stroke-width="2"/><path d="M12 7v5l3 2" stroke="#fff" stroke-width="2" fill="none"/></svg></span>
      <div>Opening Hours<br><b>Mon - Sat : 09.00 - 18.00</b></div>
    </div>
    <div class="info-item" style="left:858px">
      <span class="info-icon"><svg width="18" height="18" viewBox="0 0 24 24"><rect x="4" y="5" width="16" height="15" fill="none" stroke="#fff" stroke-width="2"/><path d="M4 10h16M8 3v4M16 3v4" stroke="#fff" stroke-width="2"/></svg></span>
      <div>Free Oral Screening<br><b>From Nov 10 &amp; 30</b></div>
    </div>
  </div>
  <div class="hero-title">
    <div class="welcome">Welcome to</div>
    <div class="brand">THE DENTAL CORNER<small>OF BRINDLEWOOD</small></div>
    <div class="tagline">BEAUTIFUL SMILE<br>BEGINS HERE</div>
  </div>
  <a class="btn">Fix Appointment</a>
  <form class="consult">
    <h3>Free Consultation</h3>
    <label>Email</label><div class="field"></div>
    <label>Phone</label><div class="field"></div>
    <label>Doctor</label><div class="field">Doctor</div>
    <span class="btn">Make Appointment</span>
  </form>
</section>

<section class="about">
  <span class="mark"></span>
  <div class="welcome-to">Welcome to the</div>
  <div class="brand">THE DENTAL CORNER<br>OF BRINDLEWOOD</div>
  <p style="top:206px">Lorem ipsum dolor sit amet, enim detracto vulputate eum ad, discere eruditi alienum cu per. No case habeo has, duo ne iusto quidam volutpat. Cu iusto ignota has, eum aperiam legimus vituperatoribus eu, mea et accusam.</p>
  <p style="top:292px">Sed cu tollit tincidunt. Ne est omnesque assentior. Mei purto omnis putent ne, ad est augue possim, vis modo splendide eu. Cu iusto ignota has, eum aperiam legimus vituperatoribus eu, mea et accusam interpretaris.</p>
  <a class="btn">Read more</a>
  <div class="video">
    <div class="video-still" role="img" aria-label="Video still of a smiling child during a dental check-up"></div>
    <span class="play"><svg width="60" height="42" viewBox="0 0 60 42"><path d="M24 13l14 8-14 8z" fill="#fff"/></svg></span>
  </div>
</section>

<section class="smile">
  <div class="smile-photo" role="img" aria-label="Smiling dentist with arms crossed in a clinic"></div>
  <h2 class="h-light">Make your</h2>
  <h2 class="h-bold">Smile brighter</h2>
  <div class="call-box">
    <div class="label">CALL TO MAKE AN APPOINTMENT</div>
    <div class="phone">1-888-555-0142</div>
  </div>
  <div class="keep">Keep in Touch with us</div>
  <div class="socials"><span></span><span></span><span></span></div>
</section>

<section class="services" role="region" aria-label="Our services">
  <h2>Our Services</h2>
  <h3>DENTAL TREATMENTS</h3>
  <p class="intro">Lorem ipsum dolor sit amet, enim detracto vulputate eum ad, discere eruditi alienum cu per. No case habeo has, duo ne iusto quidam volutpat. Cu iusto ignota has, eum aperiam legimus vituperatoribus eu, mea et accusam interpretarisPerpetua eloquentiam dissentiunt in vix, nam ut munere fabulas. Ei nec tussati noluisse Sed cu tollit tincidunt. Ne est omnesque assentior. Mei purto omnis putent ne.</p>

  <article class="card" style="left:66px">
    <svg class="icon" width="60" height="64" viewBox="0 0 60 64"><path d="M14 6c-8 0-11 8-10 16 1 8 5 12 6 22 1 8 4 16 8 16 4 0 4-14 12-14s8 14 12 14 7-8 8-16c1-10 5-14 6-22 1-8-2-16-10-16-6 0-10 4-16 4S20 6 14 6z" fill="none" stroke="#1b5fb0" stroke-width="2.5"/></svg>
    <h4>PREVENTIVE DENTISTRY</h4>
    <ul>
      <li><svg width="18" height="14" viewBox="0 0 18 14"><path d="M2 7l5 5 9-10" stroke="#8cc63f" stroke-width="3" fill="none"/></svg>Cleaning</li>
      <li><svg width="18" height="14" viewBox="0 0 18 14"><path d="M2 7l5 5 9-10" stroke="#8cc63f" stroke-width="3" fill="none"/></svg>Dental Exams</li>
      <li><svg width="18" height="14" viewBox="0 0 18 14"><path d="M2 7l5 5 9-10" stroke="#8cc63f" stroke-width="3" fill="none"/></svg>Dental Xrays</li>
      <li><svg width="18" height="14" viewBox="0 0 18 14"><path d="M2 7l5 5 9-10" stroke="#8cc63f" stroke-width="3" fill="none"/></svg>Oral hygiene</li>
      <li><svg width="18" height="14" viewBox="0 0 18 14"><path d="M2 7l5 5 9-10" stroke="#8cc63f" stroke-width="3" fill="none"/></svg>Dental Exams</li>
      <li><svg width="18" height="14" viewBox="0 0 18 14"><path d="M2 7l5 5 9-10" stroke="#8cc63f" stroke-width="3" fill="none"/></svg>Dental Xrays</li>
    </ul>
    <span class="plus"><svg width="48" height="48" viewBox="0 0 48 48"><path d="M24 14v20M14 24h20" stroke="#fff" stroke-width="3"/></svg></span>
  </article>

  <article class="card" style="left:431px">
    <svg class="icon" width="60" height="64" viewBox="0 0 60 64"><path d="M12 6c-6 0-8 6-7 12 1 6 5 8 7 12h36c2-4 6-6 7-12 1-6-1-12-7-12-5 0-8 3-12 3h-12c-4 0-7-3-12-3z" fill="none" stroke="#1b5fb0" stroke-width="2.5"/><path d="M26 30v22M34 30v22M22 38h16M22 46h16" stroke="#1b5fb0" stroke-width="2.5"/></svg>
    <h4>RESTORATIVE DENTISTRY</h4>
    <ul>
      <li><svg width="18" height="14" viewBox="0 0 18 14"><path d="M2 7l5 5 9-10" stroke="#8cc63f" stroke-width="3" fill="none"/></svg>Dental Implants</li>
      <li><svg width="18" height="14" viewBox="0 0 18 14"><path d="M2 7l5 5 9-10" stroke="#8cc63f" stroke-width="3" fill="none"/></svg>Child Dentistry</li>
      <li><svg width="18" height="14" viewBox="0 0 18 14"><path d="M2 7l5 5 9-10" stroke="#8cc63f" stroke-width="3" fill="none"/></svg>Braces</li>
      <li><svg width="18" height="14" viewBox="0 0 18 14"><path d="M2 7l5 5 9-10" stroke="#8cc63f" stroke-width="3" fill="none"/></svg>Bridges</li>
      <li><svg width="18" height="14" viewBox="0 0 18 14"><path d="M2 7l5 5 9-10" stroke="#8cc63f" stroke-width="3" fill="none"/></svg>Crowns</li>
      <li><svg width="18" height="14" viewBox="0 0 18 14"><path d="M2 7l5 5 9-10" stroke="#8cc63f" stroke-width="3" fill="none"/></svg>Whitening</li>
    </ul>
    <span class="plus"><svg width="48" height="48" viewBox="0 0 48 48"><path d="M24 14v20M14 24h20" stroke="#fff" stroke-width="3"/></svg></span>
  </article>

  <article class="card" style="left:794px">
    <svg class="icon" width="60" height="64" viewBox="0 0 60 64"><path d="M14 6c-8 0-11 8-10 16 1 8 5 12 6 22 1 8 4 16 8 16 4 0 4-14 12-14s8 14 12 14 7-8 8-16c1-10 5-14 6-22 1-8-2-16-10-16-6 0-10 4-16 4S20 6 14 6z" fill="none" stroke="#1b5fb0" stroke-width="2.5"/></svg>
    <h4>COSMETIC DENTISTRY</h4>
    <ul>
      <li><svg width="18" height="14" viewBox="0 0 18 14"><path d="M2 7l5 5 9-10" stroke="#8cc63f" stroke-width="3" fill="none"/></svg>Cleaning</li>
      <li><svg width="18" height="14" viewBox="0 0 18 14"><path d="M2 7l5 5 9-10" stroke="#8cc63f" stroke-width="3" fill="none"/></svg>Dental Exams</li>
      <li><svg width="18" height="14" viewBox="0 0 18 14"><path d="M2 7l5 5 9-10" stroke="#8cc63f" stroke-width="3" fill="none"/></svg>Dental Xrays</li>
      <li><svg width="18" height="14" viewBox="0 0 18 14"><path d="M2 7l5 5 9-10" stroke="#8cc63f" stroke-width="3" fill="none"/></svg>Oral hygiene</li>
      <li><svg width="18" height="14" viewBox="0 0 18 14"><path d="M2 7l5 5 9-10" stroke="#8cc63f" stroke-width="3" fill="none"/></svg>Dental Exams</li>
      <li><svg width="18" height="14" viewBox="0 0 18 14"><path d="M2 7l5 5 9-10" stroke="#8cc63f" stroke-width="3" fill="none"/></svg>Dental Xrays</li>
    </ul>
    <span class="plus"><svg width="48" height="48" viewBox="0 0 48 48"><path d="M24 14v20M14 24h20" stroke="#fff" stroke-width="3"/></svg></span>
  </article>
</section>

<section class="testimonials">
  <h2>What Our Clients Say</h2>
  <div class="avatar" style="left:161px;top:196px" role="img" aria-label="Portrait of client Martin Doyle"></div>
  <blockquote class="quote" style="left:271px">Lorem ipsum dolor sit amet, consectetur adipiscing elit. Quid autem habent admirationis, cum prope accesseris? An hoc usque quaque.<div class="name">- Martin Doyle</div></blockquote>
  <div class="avatar" style="left:658px;top:196px" role="img" aria-label="Portrait of client Jenna Ruiz"></div>
  <blockquote class="quote" style="left:766px">Lorem ipsum dolor sit amet, consectetur adipiscing elit. Quid autem habent admirationis, cum prope accesseris? An hoc usque quaque.<div class="name">- Jenna Ruiz</div></blockquote>
</section>

<section class="map" role="img" aria-label="Street map showing the clinic location">
  <div class="map-label">
    <svg width="26" height="34" viewBox="0 0 26 34"><path d="M13 1C6 1 1 6 1 13c0 9 12 20 12 20s12-11 12-20C25 6 20 1 13 1z" fill="#e53935"/><circle cx="13" cy="13" r="4.5" fill="#fff"/></svg>
    The Dental Corner<br>of Brindlewood
  </div>
</section>

<footer class="site-footer">
  <div class="brand">THE DENTAL CORNER<br>OF BRINDLEWOOD</div>
  <div class="spanish">SE HABLA<br>ESPAÑOL</div>
  <div class="foot-col" style="left:420px">
    <h4>CONTACT INFORMATION</h4>
    <div style="display:flex;gap:14px">
      <svg width="22" height="30" viewBox="0 0 26 34"><path d="M13 1C6 1 1 6 1 13c0 9 12 20 12 20s12-11 12-20C25 6 20 1 13 1z" fill="#8cc63f"/><circle cx="13" cy="13" r="4.5" fill="#262829"/></svg>
      <p><span class="addr-title">ADDRESS</span><br>Dental Clinic at Brindlewood now open<br>4120 Orchard Row,<br>#115 Brindlewood, FL 33000</p>
    </div>
    <p class="call-label">Call to Make an appointment</p>
    <p class="call-phone">1-888-555-0142</p>
  </div>
  <div class="foot-col" style="left:751px;width:330px">
    <h4>LOOKING FOR A GOOD DOCTOR</h4>
    <p>Lorem ipsum dolor sit amet, consectetur adipiscing elit. Quid autem habent admirationis, cum prope accesseris?</p>
    <span class="btn">MAKE APPOINTMENT</span>
    <p class="keep">Keep in Touch with us</p>
    <div class="socials"><span></span><span></span><span></span></div>
    <div class="insurance"><svg width="26" height="20" viewBox="0 0 26 20"><path d="M2 10l8 8 14-16" stroke="#8cc63f" stroke-width="3" fill="none"/></svg>All insurance accepted</div>
  </div>
</footer>
<div class="copyright">© 2019 thedentalcornerofbrindlewood All Right Reserved</div>

</body>
</html>
```